Book cover design for my new Bankruptcy Law Book

Hi

I would like to get a unique and nice design for my new book titled: "Quiet Harbors and the Lantern Keeper's Final Season".

I like blue color. It will be in Arabic so I care the most about the design of the book cover and not the words on the cover as the printing company will handle the rest.

Much appreciated,

KAREEM HADDAWI

Colors
0692cd
33a6d7
86cae7
85abd2
3277b5
0255a3

Requirements
Must have
• Blue color
Nice to have
• pictures or shapes related to bankruptcy or insolvency

```html
<!DOCTYPE html>
<html lang="en">
<head>
<meta charset="utf-8">
<title>Quiet Harbors and the Lantern Keeper's Final Season — Cover</title>
<link href="https://fonts.googleapis.com/css2?family=League+Gothic&family=Sorts+Mill+Goudy:ital@1&display=swap" rel="stylesheet">
<style>
  :root {
    --sky-top: #86a6bb;
    --sky-mid: #6f8f95;
    --sage: #7f9c8a;
    --cream: #d9d7a8;
    --bar-light: #ecebc2;
    --bar-shade: #bcd7bf;
    --grid-line: rgba(220, 232, 225, 0.45);
    --arrow: #d5955b;
    --arrow-dark: #c97e48;
    --title: #ffffff;
    --title-shadow: rgba(30, 45, 50, 0.45);
    --photo-dark: #2a2530;
    --photo-warm: #6b4a3a;
    --monitor: #4d4358;
  }
  html, body {
    margin: 0;
    padding: 0;
    overflow: hidden;
    background: #ffffff;
  }
  .cover {
    position: relative;
    width: 802px;
    height: 1200px;
    overflow: hidden;
    background: linear-gradient(180deg, var(--sky-top) 0%, var(--sky-mid) 38%, var(--sage) 58%, var(--cream) 100%);
  }
  .chart {
    position: absolute;
    inset: 0;
  }
  .title {
    position: absolute;
    left: 0;
    right: 0;
    margin: 0;
    text-align: center;
    color: var(--title);
    text-shadow: 3px 4px 4px var(--title-shadow);
    white-space: nowrap;
  }
  .title--block {
    font-family: "League Gothic", "Oswald", sans-serif;
    font-weight: 400;
    text-transform: uppercase;
    line-height: 1;
    letter-spacing: 1px;
  }
  .title--lead { top: 34px; font-size: 162px; }
  .title--link {
    top: 190px;
    font-family: "Sorts Mill Goudy", Georgia, serif;
    font-style: italic;
    font-size: 50px;
    line-height: 1;
  }
  .title--main { top: 242px; font-size: 212px; letter-spacing: 3px; }
  .title--tail { top: 428px; font-size: 100px; }
  .photo {
    position: absolute;
  }
  .photo--person {
    left: 350px;
    top: 575px;
    width: 452px;
    height: 625px;
    background: linear-gradient(170deg, var(--photo-warm) 0%, var(--photo-dark) 55%, #1b1a20 100%);
    border-radius: 180px 140px 0 0;
  }
  .photo--monitor {
    left: 0;
    top: 888px;
    width: 370px;
    height: 312px;
    background: linear-gradient(180deg, var(--monitor) 0%, #3a3344 100%);
  }
</style>
</head>
<body>
<main class="cover">
  <svg class="chart" width="802" height="1200" viewBox="0 0 802 1200" aria-hidden="true">
    <defs>
      <linearGradient id="bar-fill" x1="0" y1="0" x2="1" y2="0">
        <stop offset="0" stop-color="var(--bar-light)"/>
        <stop offset="0.5" stop-color="var(--bar-shade)"/>
        <stop offset="1" stop-color="var(--bar-light)"/>
      </linearGradient>
      <filter id="arrow-shadow" x="-10%" y="-10%" width="130%" height="140%">
        <feDropShadow dx="4" dy="6" stdDeviation="4" flood-color="#2e3a36" flood-opacity="0.35"/>
      </filter>
    </defs>
    <g class="chart__grid" stroke="var(--grid-line)" stroke-width="1.5">
      <line x1="62" y1="0" x2="62" y2="1200"/>
      <line x1="157" y1="0" x2="157" y2="1200"/>
      <line x1="251" y1="0" x2="251" y2="1200"/>
      <line x1="346" y1="0" x2="346" y2="1200"/>
      <line x1="440" y1="0" x2="440" y2="1200"/>
      <line x1="535" y1="0" x2="535" y2="1200"/>
      <line x1="629" y1="0" x2="629" y2="1200"/>
      <line x1="724" y1="0" x2="724" y2="1200"/>
    </g>
    <g class="chart__bars" fill="url(#bar-fill)" opacity="0.85">
      <rect x="0" y="618" width="52" height="582"/>
      <rect x="72" y="662" width="62" height="538"/>
      <rect x="154" y="718" width="62" height="482"/>
      <rect x="236" y="773" width="62" height="427"/>
      <rect x="318" y="830" width="62" height="370"/>
      <rect x="400" y="880" width="32" height="320"/>
    </g>
    <g class="chart__trend" filter="url(#arrow-shadow)">
      <polyline points="104,570 198,650 262,590 350,672" fill="none" stroke="var(--arrow)" stroke-width="30" stroke-linejoin="miter"/>
      <polygon points="333,690 376,654 378,703" fill="var(--arrow)"/>
      <polygon points="336,655 378,703 346,702" fill="var(--arrow-dark)"/>
    </g>
  </svg>

  <h1 class="title title--block title--lead">Quiet Harbors</h1>
  <p class="title title--link">and the Lantern Keeper's</p>
  <p class="title title--block title--main">Final</p>
  <p class="title title--block title--tail">Season</p>

  <div class="photo photo--person" role="img" aria-label="Photograph of a worried man resting his face in his hands in front of a computer"></div>
  <div class="photo photo--monitor" role="img" aria-label="Photograph of a computer monitor seen from behind"></div>
</main>
</body>
</html>
```